Exhibition Print

Need to have a few video meetings and work scope
we have approx 20 panels that need to tell a story of our business
I have updated a story board'
Our main company is:
trelvon.com.au fibre to the home technologies for new or greenfield retirement estates and ethernet over copper for existing retirement estates

We will pay for the extra meetings on top

so the design needs approx 20 panels 2.4m HEIGHT x 1m WIDE
so we will work out the correct way to price this together

Target Market(s)

retirement communiites

Industry/Entity Type

retirement and communication technologies

Requirements
Nice to have
• i have attached a story board

```html
<!DOCTYPE html>
<html lang="en">
<head>
<meta charset="utf-8">
<title>Trelvon Health – Exhibition Panels</title>
<link rel="stylesheet" href="https://fonts.googleapis.com/css2?family=Montserrat:wght@500;600;700&display=swap">
<style>
  :root {
    --stage: #161c26;
    --brand-green: #55a148;
    --brand-blue: #2f74b1;
    --paper: #ffffff;
    --logo-green: #4f9a3f;
  }
  html, body {
    margin: 0;
    padding: 0;
    width: 1200px;
    height: 1200px;
    overflow: hidden;
    background: var(--stage);
    font-family: "Montserrat", Arial, sans-serif;
  }
  .canvas {
    position: relative;
    width: 1200px;
    height: 1200px;
  }
  .panel {
    position: absolute;
    top: 100px;
    width: 417px;
    height: 1000px;
    box-shadow: 0 22px 28px -16px rgba(0,0,0,0.75);
  }
  .panel--connected { left: 163px; }
  .panel--values { left: 620px; }
  .panel svg { display: block; width: 417px; height: 1000px; }
  .logo-name { font-weight: 700; font-size: 26px; fill: var(--brand-blue); }
  .logo-tagline { font-weight: 600; font-size: 10px; fill: var(--logo-green); }
  .headline { font-weight: 700; font-size: 38px; fill: var(--paper); }
  .body-copy { font-weight: 500; font-size: 17px; fill: var(--paper); }
</style>
</head>
<body>
<main class="canvas">

  <section class="panel panel--connected">
    <svg viewBox="0 0 417 1000" xmlns="http://www.w3.org/2000/svg">
      <defs>
        <linearGradient id="photoCouple" x1="0" y1="0" x2="1" y2="1">
          <stop offset="0" stop-color="#d9d9d7"/>
          <stop offset="0.5" stop-color="#a08c78"/>
          <stop offset="1" stop-color="#c9a27a"/>
        </linearGradient>
      </defs>
      <rect class="panel-field" width="417" height="1000" fill="var(--brand-green)"/>
      <polygon class="accent-stripe" points="0,520 417,440 417,1000 0,1000" fill="var(--brand-blue)"/>
      <polygon class="photo-area" role="img" aria-label="Photo of a smiling senior couple sitting together looking at a laptop"
               points="0,534 417,454 417,1000 0,1000" fill="url(#photoCouple)"/>
      <g class="logo-plate">
        <polygon points="0,40 330,40 305,120 0,120" fill="var(--paper)"/>
        <rect x="36" y="62" width="22" height="22" fill="var(--brand-blue)"/>
        <text class="logo-name" x="68" y="83">Trelvon health</text>
        <text class="logo-tagline" x="70" y="104">Specialists in Telecommunication</text>
      </g>
      <text class="headline" x="36" y="200">We Keep</text>
      <text class="headline" x="36" y="246">You Connected</text>
      <text class="body-copy" x="38" y="292">Trelvon Health keeps</text>
      <text class="body-copy" x="38" y="316">retirement communities</text>
      <text class="body-copy" x="38" y="340">connected through</text>
      <text class="body-copy" x="38" y="364">future-ready telecom</text>
      <text class="body-copy" x="38" y="388">and care solutions</text>
    </svg>
  </section>

  <section class="panel panel--values">
    <svg viewBox="0 0 417 1000" xmlns="http://www.w3.org/2000/svg">
      <defs>
        <linearGradient id="photoCare" x1="0" y1="0" x2="1" y2="1">
          <stop offset="0" stop-color="#e9e3da"/>
          <stop offset="0.5" stop-color="#c7a893"/>
          <stop offset="1" stop-color="#8fcbcc"/>
        </linearGradient>
      </defs>
      <rect class="panel-field" width="417" height="1000" fill="var(--brand-blue)"/>
      <polygon class="accent-stripe" points="0,520 417,440 417,1000 0,1000" fill="var(--brand-green)"/>
      <polygon class="photo-area" role="img" aria-label="Photo of a young carer showing a tablet to a smiling older woman"
               points="0,534 417,454 417,1000 0,1000" fill="url(#photoCare)"/>
      <g class="logo-plate">
        <polygon points="0,40 330,40 305,120 0,120" fill="var(--paper)"/>
        <rect x="36" y="62" width="22" height="22" fill="var(--brand-blue)"/>
        <text class="logo-name" x="68" y="83">Trelvon health</text>
        <text class="logo-tagline" x="70" y="104">Specialists in Telecommunication</text>
      </g>
      <text class="headline" x="36" y="200">People-Centric</text>
      <text class="headline" x="36" y="246">Values</text>
      <text class="body-copy" x="38" y="292">Dedication, Communication,</text>
      <text class="body-copy" x="38" y="316">Passion.</text>
      <text class="body-copy" x="38" y="340">Personalized local support</text>
    </svg>
  </section>

</main>
</body>
</html>
```